Layout of a 14-page report

I need a professional, well-designed, layout for a 14-page free report I'm offering.
My colors are red/black/white and have a chalkboard theme in my header graphic which you can incorporate if you want: see my website here - http://larkavell.example/. I am an SEO strategy consultant and this report is about "Ranking Basics."
The attachment contains a few images/designs and graphics I like that may help guide your creative process.
I would like to see the:
1. Cover page
2. inside spread layout of a standard page
3. inside spread layout of a "page with sidebar content" (indicated in the attachment)
The selected winner will complete all pages. Thank you!

```html
<!DOCTYPE html>
<html lang="en">
<head>
<meta charset="utf-8">
<title>Ranking Basics – Report Layout</title>
<link href="https://fonts.googleapis.com/css2?family=Anton&family=Oswald:wght@400;600;700&family=Bangers&family=Open+Sans:ital,wght@0,400;0,600;0,700;0,800;1,400&family=Permanent+Marker&display=swap" rel="stylesheet">
<style>
:root{
  --red:#d3141b;
  --red-dark:#a80d12;
  --black:#111111;
  --chalk:#2b2b2b;
  --white:#ffffff;
  --paper:#ffffff;
  --ink:#222222;
  --grey:#6b6b6b;
  --yellow:#f2c21b;
  --green:#5aa832;
  --tint:#fdeaea;
}
*{box-sizing:border-box;margin:0;padding:0}
html,body{width:1200px;height:2474px;overflow:hidden;background:var(--white)}
body{position:relative;font-family:"Open Sans",Arial,sans-serif;color:var(--ink)}
.page{position:absolute;background:var(--paper);overflow:hidden;box-shadow:0 0 0 1px #e2e2e2}

/* cover */
.cover{left:262px;top:12px;width:676px;height:838px;background:var(--black)}
.cover-title{position:absolute;left:22px;top:20px;width:310px;height:200px;background:var(--red);padding:14px 16px 0}
.cover-title h1{font-family:"Anton",Impact,sans-serif;color:var(--white);font-size:56px;line-height:1;font-weight:400;text-transform:uppercase}
.cover-sub{position:absolute;left:22px;top:200px;width:310px;background:var(--white);color:var(--red);font-family:"Anton",Impact,sans-serif;font-size:34px;line-height:1.05;padding:8px 16px 10px;text-transform:uppercase}
.cover-kicker{position:absolute;left:350px;top:18px;width:310px;font-family:"Oswald",Arial,sans-serif;color:var(--white);font-size:34px;line-height:1.1}
.cover-kicker .hl{color:var(--red);font-weight:700}
.cover-art{position:absolute;left:0;top:300px;width:676px;height:538px;background:radial-gradient(circle at 50% 50%,#585858 0%,#333 45%,#1c1c1c 100%)}
.cover-wheel{position:absolute;left:148px;top:90px;width:380px;height:380px;border-radius:50%;background:radial-gradient(circle,#fff 0%,#eee 40%,#c8101a 41%,#9d0c12 60%,#222 61%,#222 100%);opacity:.9}

/* shared inner page */
.page-head{position:absolute;left:0;top:0;width:100%;height:64px;background:var(--black)}
.page-head .swoop{position:absolute;right:0;top:0;height:64px}
.page-head h2{position:absolute;left:24px;top:8px;font-family:"Bangers",Impact,sans-serif;font-weight:400;font-size:44px;letter-spacing:2px;color:var(--white);text-transform:uppercase;line-height:1}
.page-foot{position:absolute;left:0;bottom:0;width:100%;height:34px;background:var(--red);display:flex;align-items:center;justify-content:space-between;padding:0 22px;color:var(--white);font-size:11px;font-weight:700}
.page-foot .site{font-size:14px;letter-spacing:.5px}
.page-body{position:absolute;left:26px;right:26px}
p{font-size:10px;line-height:1.45;margin-bottom:7px}

/* contents page */
.contents{left:0;top:862px;width:595px;height:738px}
.toc-title{font-family:"Oswald",Arial,sans-serif;font-size:19px;font-weight:600;margin-bottom:10px}
.toc{list-style:none}
.toc li{display:flex;align-items:flex-start;gap:8px;font-family:"Oswald",Arial,sans-serif;font-size:17px;line-height:1.2;margin-bottom:6px}
.num{flex:none;width:18px;height:18px;border-radius:50%;background:var(--red);color:var(--white);font-size:11px;font-weight:700;display:flex;align-items:center;justify-content:center;margin-top:1px;font-family:"Open Sans",Arial,sans-serif}
.toc-extra{font-family:"Oswald",Arial,sans-serif;font-size:18px;font-weight:700;line-height:1.3;text-transform:uppercase;margin-top:6px}
.toc-photo{position:absolute;left:0;top:470px;width:560px;height:200px;background:linear-gradient(160deg,#f4f4f4 0%,#d9d9d9 60%,#f0d0d0 100%)}

/* intro page */
.intro{left:605px;top:862px;width:595px;height:738px}
.intro h3{font-family:"Oswald",Arial,sans-serif;color:var(--red);font-size:19px;text-align:center;font-weight:700;margin-bottom:8px}
.dropcap{float:left;font-family:"Anton",Impact,sans-serif;font-size:50px;line-height:.9;margin:2px 6px 0 0}
.lead-q{font-size:13px;font-weight:800;text-align:center;line-height:1.25;margin:4px 0 8px}
.intro h4{font-family:"Oswald",Arial,sans-serif;color:var(--red);font-size:17px;text-align:center;margin:4px 0 6px}
.intro h5{font-size:13px;font-weight:800;margin:4px 0 4px}
.ticks{list-style:none;margin:2px 0 6px 24px}
.ticks li{font-size:10px;line-height:1.5;position:relative;padding-left:12px}
.ticks li::before{content:"";position:absolute;left:0;top:5px;width:5px;height:5px;background:var(--red);border-radius:50%}
.callout{font-size:12px;font-weight:800;text-align:center;line-height:1.3;margin-top:6px}
.callout em{color:var(--red)}
.bar{background:var(--black);color:var(--white);font-size:10px;font-weight:700;text-align:center;padding:4px;margin-top:6px}
.simple{font-size:13px;text-align:center;color:var(--grey);margin-top:10px}
.started{font-family:"Permanent Marker",cursive;color:var(--red);font-size:30px;text-align:center}

/* step pages */
.step1{left:0;top:1612px;width:595px;height:862px}
.step2{left:605px;top:1612px;width:595px;height:862px}
.step-tag{position:absolute;top:12px;font-family:"Bangers",Impact,sans-serif;font-size:42px;color:var(--black);padding:2px 24px;line-height:1}
.step1 .step-tag{left:0;background:var(--yellow)}
.step2 .step-tag{right:0;background:var(--green);color:var(--white)}
.step-badge{position:absolute;top:10px;width:74px;height:74px;border-radius:50%;border:5px solid var(--red);font-family:"Anton",Impact,sans-serif;font-size:40px;display:flex;align-items:center;justify-content:center}
.step1 .step-badge{left:260px;background:var(--yellow)}
.step2 .step-badge{left:260px;background:var(--green);color:var(--white)}
.step-title{font-family:"Oswald",Arial,sans-serif;font-size:17px;font-weight:700;margin-bottom:8px}
.step-title .r{color:var(--red)}
.sidebar{float:right;width:190px;margin:0 0 8px 12px;border:2px solid var(--red);background:var(--tint);padding:8px;font-size:10px;line-height:1.4}
.sidebar b{display:block;font-weight:800;text-align:right;margin-bottom:4px}
.sidebar .red{color:var(--red);font-weight:700}
.qhead{font-size:12px;font-weight:800;margin:6px 0}
.qlist{list-style:none}
.qlist li{display:flex;gap:8px;font-size:10px;line-height:1.35;margin-bottom:5px}
.qlist .num{width:15px;height:15px;font-size:9px;background:var(--yellow);color:var(--black)}
.ask{font-size:12px;font-weight:800;text-align:center;color:var(--red);margin-top:10px}
.closing{font-size:17px;font-weight:800;text-align:center;line-height:1.25;margin-top:14px}
.quote-mark{float:left;font-family:"Anton",Impact,sans-serif;font-size:60px;line-height:.8;color:var(--grey);margin-right:6px}
.indent{margin-left:50px}
.verdict{display:flex;align-items:center;gap:10px;margin:6px 0}
.verdict .tag{flex:none;width:82px;height:42px;display:flex;align-items:center;justify-content:center;font-family:"Anton",Impact,sans-serif;font-size:30px;color:var(--white)}
.yes{background:var(--green)}
.no{background:var(--black)}
.remember{font-family:"Oswald",Arial,sans-serif;color:var(--red);font-size:19px;font-weight:700;text-align:center;margin-top:8px}
.remember-sub{font-size:13px;font-weight:800;text-align:center;margin-top:4px}
.would-art{position:absolute;left:300px;top:720px;width:280px;height:104px;background:linear-gradient(120deg,#5f7f3a 0%,#9bc25a 100%)}
</style>
</head>
<body>

<section class="page cover" aria-label="Cover page">
  <div class="cover-title"><h1>Getting Serious About SEO</h1></div>
  <div class="cover-sub">How to get<br>more leads</div>
  <div class="cover-kicker">A Checklist of <span class="hl">8 ESSENTIALS</span> for Busy Marketers in Growing Businesses</div>
  <div class="cover-art" role="img" aria-label="Chalkboard illustration: a wheel of eight numbered badges around the Ranking Basics emblem">
    <div class="cover-wheel"></div>
  </div>
</section>

<section class="page contents" aria-label="Table of contents">
  <header class="page-head">
    <svg class="swoop" width="200" height="64" viewBox="0 0 200 64"><path d="M60 0 Q120 40 200 20 L200 0Z" fill="var(--red)"/></svg>
    <h2>Table of Contents</h2>
  </header>
  <div class="page-body" style="top:86px">
    <div class="toc-title">INTRODUCTION: A Checklist of Ranking Basics</div>
    <ol class="toc">
      <li><span class="num">1</span>Explore Motivations, Determine KPIs, Manage Expectations</li>
      <li><span class="num">2</span>“Would You Give This Site Your Credit Card?”</li>
      <li><span class="num">3</span>Website Marketing Fundamentals: Engagement</li>
      <li><span class="num">4</span>SEO’s Foundational Individual Elements</li>
      <li><span class="num">5</span>Take a Holistic View: Benchmark Individual Elements and Then the Site as a Whole</li>
      <li><span class="num">6</span>Getting Lead Gen Results</li>
      <li><span class="num">7</span>Foundational SEO: Your First Order of Business</li>
      <li><span class="num">8</span>Integrate Ongoing SEO into Marketing Routine</li>
    </ol>
    <div class="toc-extra">Summary<br>About Lark<br>Resource Links</div>
  </div>
  <div class="toc-photo" role="img" aria-label="Photo of a hand drawing a rising bar chart with a red arrow"></div>
  <footer class="page-foot"><span>lark@larkavell.example</span><span class="site">www.larkavell.example</span><span>@larkavell</span></footer>
</section>

<section class="page intro" aria-label="Introduction page">
  <header class="page-head">
    <svg class="swoop" width="200" height="64" viewBox="0 0 200 64"><path d="M60 0 Q120 40 200 20 L200 0Z" fill="var(--red)"/></svg>
    <h2>Introduction</h2>
  </header>
  <div class="page-body" style="top:80px">
    <h3>A Checklist of Ranking Basics</h3>
    <p><span class="dropcap">F</span>or my clients and the marketers I am acquainted with, time is their most precious resource. They have to guard their time like a building. And within this limited time, they have the fun challenge of being expected to consistently produce more and better results. And the really good marketers, well, they don’t solely want results. They want to make a contribution, become better at their craft, and genuinely help their organization grow by driving more traffic, awareness, and of course leads.</p>
    <div class="lead-q">The beauty of search engine optimization (SEO) is it helps with all of the above: efficiency, results, contribution, growth and leads.</div>
    <p>But when it comes to effectively deploying SEO and hitting KPIs and objectives, marketers are often held back by a lack of time, resources, and knowledge about where to even begin.</p>
    <h4>SEO: Simple, But Not Easy</h4>
    <p>I personally dislike the phrase “simple but not easy.” A statement like that needs to be backed up with a more detailed explanation, don’t you think? It makes my brain hurt to think about the implications and makes me wish someone would just spell out what is not so easy so I know what I’m getting into. That being said…</p>
    <h5>…SEO is simple but not easy.</h5>
    <p>I truly believe that SEO is simpler than ever, but not easy, due to the multiple disciplines and activities that have to come together in order to realize long-term, sustainable success. SEO success today requires a mix of best practices, trends, marketing 101, and fundamentals meshed together.</p>
    <p>But believe me, the headache is worth it. If you…</p>
    <ul class="ticks">
      <li>Know you’re missing opportunities</li>
      <li>Want to attract a certain type of customer but aren’t sure how</li>
      <li>Are overly dependent on pricey paid marketing avenues like PPC at the expense of organic SEO or other lower cost alternatives</li>
      <li>Have tried SEO but got busy and you know the shop-and-go efforts won’t produce results you know are attainable</li>
    </ul>
    <p>…then this guide is for you.</p>
    <div class="callout">In this 8-point checklist I’ll explain the essential elements of SEO and <em>HOW TO GENERATE MORE LEADS TO YOUR SITE CONSISTENTLY.</em></div>
    <div class="bar">All it takes is a solid start, a plan for consistent action, and time and momentum in the right direction.</div>
    <div class="simple">Simple, right?</div>
    <div class="started">Let’s get started.</div>
  </div>
  <footer class="page-foot"><span>lark@larkavell.example</span><span class="site">www.larkavell.example</span><span>@larkavell</span></footer>
</section>

<section class="page step1" aria-label="Step 1 page">
  <header class="page-head" style="height:96px">
    <svg class="swoop" width="595" height="96" viewBox="0 0 595 96" style="height:96px;left:0"><path d="M0 70 Q300 110 595 60 L595 96 L0 96Z" fill="var(--red)"/></svg>
    <div class="step-tag">Step 1</div>
  </header>
  <div class="step-badge">1</div>
  <div class="page-body" style="top:112px">
    <div class="step-title">Explore Motivations, <span class="r">Determine KPIs, Manage Expectations</span></div>
    <p><span class="dropcap">W</span>hy are you seeking help with SEO? What are you trying to achieve? What keywords do you want? What are you wanting to see happen? What exactly is the problem? Have you ever seen SEO success? How will you know when you’ve achieved success?</p>
    <div class="sidebar"><b>What will be needed:</b><span class="red">Foundational SEO tweaking, a thorough SEO application, or a major overhaul?</span><b style="margin-top:6px">Hint:</b>For most marketers it will be that middle option.</div>
    <p>I know, I know – that’s a lot of questions.</p>
    <p>But this is where you first start when preparing your lead gen SEO strategy. The answers to these questions help you assess if you’re starting from scratch and where those priorities are. “Fixing” something that went wrong, updating a site if it hasn’t kept up with best practices. And very importantly, gauge if you (or better yet your boss) have practical expectations on timelines and efforts involved.</p>
    <div class="qhead">Use these questions as a guide to help determine where you fall:</div>
    <ol class="qlist">
      <li><span class="num">1</span>What do you hope to gain by getting found online and having a better online presence?</li>
      <li><span class="num">2</span>What keywords do you want? Save a Gridsheet spreadsheet with the 5-10 most important.</li>
      <li><span class="num">3</span>Why do you think your SEO efforts haven’t worked so far?</li>
      <li><span class="num">4</span>How strong is your knowledge of SEO and knowing where to start? On a scale of 1-10, “1” being total newb, “5” being you know enough to know what you don’t know, and “10” being you’re skilled, updated and experienced but lack execution time and resources.</li>
      <li><span class="num">5</span>Have you ever seen SEO success?</li>
      <li><span class="num">6</span>Why is now the time to do something about it?</li>
      <li><span class="num">7</span>What do you envision will change if you gain SEO success?</li>
      <li><span class="num">8</span>What do you want to get out of your SEO efforts? List your goals and objectives.</li>
      <li><span class="num">9</span>Who has SEO work been done to the site by, your web designer, previous marketers, or an outside SEO resource?</li>
      <li><span class="num">10</span>How familiar with SEO was the person who designed your site?</li>
      <li><span class="num">11</span>When was your site last redesigned by a professional?</li>
    </ol>
    <div class="ask">HOW ARE YOU LOOKING SO FAR?</div>
    <div class="closing">At this point there’s nothing actionable to do with this information, you’re just gathering up these details for your plan.</div>
  </div>
  <footer class="page-foot"><span>lark@larkavell.example</span><span class="site">www.larkavell.example</span><span>@larkavell</span></footer>
</section>

<section class="page step2" aria-label="Step 2 page">
  <header class="page-head" style="height:96px">
    <svg class="swoop" width="595" height="96" viewBox="0 0 595 96" style="height:96px;left:0"><path d="M0 60 Q300 110 595 70 L595 96 L0 96Z" fill="var(--red)"/></svg>
    <div class="step-tag">Step 2</div>
  </header>
  <div class="step-badge">2</div>
  <div class="page-body" style="top:112px">
    <div class="step-title" style="text-align:center">Would You Give This Site Your Credit Card?</div>
    <p><span class="quote-mark">“</span><b>“Would you give this site your credit card?” This is one of a series of questions that Searchly engineers ask when evaluating sites to determine if they needed to assess a Quokka penalty.</b></p>
    <p class="indent">The Quokka update is a search filter/algorithm update that occurred in 2011. It was designed to improve the quality of search results. Quokka penalties were assessed at greatest sites with poor quality content from ranking well. Since 2011 many more iterations of Quokka have rolled out, including other algorithm changes, which reinforces Searchly’s strong warnings that spam, manipulative tactics and low-quality SEO work activities will not be tolerated.</p>
    <p>So back to your credit card.</p>
    <p>Getting a site to be deemed trustworthy enough for an objective person to give their credit card information to is the bare minimum of getting to SEO success.</p>
    <p>What this really means, is that your site better look, feel, and act extremely trustworthy. Before you start your SEO endeavors (or parallel to your SEO endeavors), put yourself in a neutral position and answer objectively:</p>
    <div class="verdict"><p style="margin:0;font-size:11px"><b style="color:var(--red)">“Would you give this site your credit card?”</b> Make sure the answer is a confident “yes.” If it’s “maybe,” then that is a “no.” And if it’s a clear “no,” then update your design, put social proof on the page, get testimonials, freshen up your copy, and get clear on your messaging.</p><span class="tag yes">YES</span></div>
    <div class="verdict"><span class="tag no">NO</span><p style="margin:0">If you answered “maybe” or “no” then list out the top three most impactful things you can change or improve that will bring you closer to a confident “YES.”</p></div>
    <p>Then, to make this actionable and take it one step further, list out the person or resource who will actually do these things, the timeframe to get it done, and the cost if there’s going to be one. And of course time block this on your calendar or put it on a timeline now. What you just wrote down are priority essential activities so will be in your Phase 1 plan.</p>
    <div class="remember">REMEMBER, YOUR SITE ISN’T GOING TO SEO ITSELF.</div>
    <div class="remember-sub">SEO today requires active upkeep and execution.</div>
  </div>
  <div class="would-art" role="img" aria-label="Three-dimensional green lettering asking Would You?"></div>
  <footer class="page-foot"><span>lark@larkavell.example</span><span class="site">www.larkavell.example</span><span>@larkavell</span></footer>
</section>

</body>
</html>
```